Design a Google site for a travel agency

I own a travel agency and I would like to have a Google site built for my company called Wavetrailjourneys.example by Brisk Harbor Getaways. Our specialty Cruising and adventure. We create a lot of custom tour of Europe and Peru. Our Adventure tours targets mainly women from 25 to 65. I would like to site especially the cruise to appeal to family but also upscale more expensive upscale clientele.
Updates

I would like to shift away from create a new site with multiple pages to one simple Google Site page with a Contact us page and testimonials. The sites theme is Cruise & Adventure Travel. We specialize in selling cruises and building custom travel tours around the world.

Target Market(s)

Cruisers and adventure travelers for women from 25 to 70

Industry/Entity Type

travel industry with a focus on cruising and adventure travel

Coding

Coded - Design and coding required

Number of Pages Required

5+ page

Font styles to use
Serif
Sans Serif

Requirements
Must have
• Home page, Cruise, Adventure Tours, Testimonials, About Us
Nice to have
• Auto place https://www.briskharborgetaways.example/offers into the site.
Should not have
• beach resorts

```html
<!DOCTYPE html>
<html lang="en">
<head>
<meta charset="utf-8">
<title>Brisk Harbor Getaways</title>
<link rel="stylesheet" href="https://fonts.googleapis.com/css2?family=Cinzel:wght@400;500&family=Lato:wght@400;700&display=swap">
<style>
:root{
  --ink:#1d1d1d;
  --text:#333;
  --brand:#e89a1c;
  --button:#29a9e0;
  --footer:#1b1b1b;
  --orange:#f5a623;
  --rule:#9a9a9a;
  --white:#fff;
}
*{box-sizing:border-box;margin:0;padding:0}
html,body{width:1200px;height:3607px;overflow:hidden}
body{font-family:'Lato',sans-serif;color:var(--text);background:var(--white)}

.site-header{height:106px;display:flex;align-items:center;padding:0 112px}
.brand{display:flex;align-items:center;gap:10px;font-family:'Cinzel',serif;font-size:17px;line-height:1.15;color:var(--brand);font-weight:400;flex-shrink:0}
.brand-dot{width:16px;height:16px;border-radius:50%;background:var(--brand);flex-shrink:0}
.main-nav{display:flex;gap:28px;font-size:15px;color:var(--ink);margin-left:auto}

.hero{position:relative;height:601px;background:linear-gradient(180deg,#8a5a3c 0%,#5b3a2e 30%,#2c2a30 65%,#1f2630 100%)}
.hero-frame{position:absolute;left:245px;top:120px;width:710px;height:362px;border:3px solid var(--white);display:flex;flex-direction:column;align-items:center;justify-content:center;color:var(--white);font-family:'Cinzel',serif;text-align:center}
.hero-frame .welcome{font-size:42px}
.hero-frame .name{font-size:50px;font-weight:500;margin-top:6px}

.section-title{font-family:'Cinzel',serif;font-size:30px;color:var(--ink);text-align:center;font-weight:400}
.section-title.caps{text-transform:uppercase;font-size:28px}
.section-sub{text-align:center;font-size:15px;margin-top:12px;color:var(--ink)}
.btn{display:block;margin:0 auto;background:var(--button);color:var(--white);font-family:'Cinzel',serif;font-weight:500;font-size:15px;text-align:center;letter-spacing:.5px}

.experiences{height:690px;padding-top:84px}
.photo-row{display:flex;gap:36px;width:976px;margin:56px auto 0}
.photo{width:301px;height:305px}
.experiences .btn{width:149px;height:65px;line-height:65px;margin-top:34px}

.offers{height:514px;background:linear-gradient(180deg,#efe8dc 0%,#e9e0cf 50%,#e4d6bf 100%);padding-top:102px;text-align:center}
.offers p{font-size:18px;line-height:32px;color:var(--ink);width:760px;margin:48px auto 0}
.offers .btn{width:183px;height:65px;line-height:65px;margin-top:56px}

.promotions{height:632px;padding-top:96px}
.promo-grid{display:grid;grid-template-columns:repeat(3,1fr);width:1000px;margin:52px auto 0;row-gap:44px;column-gap:40px}
.promo{text-align:center}
.promo h3{font-family:'Cinzel',serif;font-weight:400;font-size:17px;line-height:27px;color:var(--ink)}
.promo p{font-size:12.5px;line-height:23px;margin-top:12px;color:var(--ink)}

.magazines{height:686px;background:linear-gradient(180deg,#f5ede6 0%,#f2ebe4 50%,#ece2d6 100%);padding-top:84px}
.magazines .btn{width:149px;height:65px;line-height:65px;margin-top:34px}

.site-footer{height:378px;background:var(--footer);padding-top:70px;color:var(--white);text-align:center}
.site-footer .brand{justify-content:center;font-size:26px}
.footer-nav{display:flex;justify-content:center;gap:26px;font-size:13px;margin-top:48px}
.social{display:flex;justify-content:center;gap:20px;margin-top:30px}
.social span{width:48px;height:48px;border-radius:50%;background:var(--orange);font-size:10px;line-height:48px;color:var(--white)}
.footer-rule{width:976px;height:1px;background:var(--rule);margin:24px auto 0}
.copyright{font-size:15px;margin-top:26px}
</style>
</head>
<body>
<header class="site-header">
  <div class="brand"><span class="brand-dot"></span><span>Brisk Harbor<br>Getaways</span></div>
  <nav class="main-nav"><span>About Us</span><span>Experiences</span><span>Tours</span><span>Offers</span><span>Blogs</span><span>Contest</span><span>Testimonials</span><span>Exclusives</span><span>Contact</span></nav>
</header>

<section class="hero" role="img" aria-label="Cliffside coastal village at sunset over the sea">
  <div class="hero-frame">
    <div class="welcome">Welcome to</div>
    <div class="name">Brisk Harbor Getaways</div>
  </div>
</section>

<section class="experiences">
  <h2 class="section-title">Popular Travel Experiences</h2>
  <p class="section-sub" style="font-size:14px">Some of our most popular travel categories</p>
  <div class="photo-row">
    <div class="photo" role="img" aria-label="River cruise ship passing a hillside town" style="background:linear-gradient(180deg,#6a9fd0 0%,#4f7e3e 40%,#8c8f86 70%,#3f6f88 100%)"></div>
    <div class="photo" role="img" aria-label="Group yoga session on the shore" style="background:linear-gradient(180deg,#b9bfc6 0%,#a9adb1 55%,#b39f8a 100%)"></div>
    <div class="photo" role="img" aria-label="Breakfast table on a ship deck overlooking the sea" style="background:linear-gradient(180deg,#a8b6c6 0%,#5d7a98 35%,#cfc8bf 70%,#e6e1da 100%)"></div>
  </div>
  <span class="btn">VIEW ALL</span>
</section>

<section class="offers" role="img" aria-label="Faded mountain valley with a hiker, behind the signup text">
  <h2 class="section-title caps">Get Amazing Offers &amp; Save Big</h2>
  <p>Get the best travel deals &amp; specials delivered directly to your inbox.<br>Sign up to receive incredible offers on cruises, adventures, all-inclusives, coach tours, family vacations and holidays of a lifetime.</p>
  <span class="btn">SUBSCRIBE NOW</span>
</section>

<section class="promotions">
  <h2 class="section-title caps">Featured Promotions</h2>
  <p class="section-sub" style="font-size:18px">The best deals happening now. Act fast, they won't last long!</p>
  <div class="promo-grid">
    <div class="promo"><h3>Starting from $879CAD<br>per person - Nashville</h3><p>5-Nights | Music, Moonshine &amp; More |<br>Nashville, Tennessee | Packages Available<br>from June 8 - December 31, 2022</p></div>
    <div class="promo"><h3>Take on a Bolder Tropic<br>Trek!</h3><p>Serenade Horizon May 14, 2023 Departure<br>| 7-Night Western Caribbean Cruise |<br>Offer Expires October 2, 2022</p></div>
    <div class="promo"><h3>Sacred Valley Trek<br>Peru - A New Women's<br>Adventure</h3><p>Small Group Tour | Cusco, Sacred Valley<br>&amp; Machu Picchu | 10 Days | Offer</p></div>
    <div class="promo"><h3>Maple Thrill Park -<br>A Family Escape</h3><p>2022 Packages | Take Your Kids to<br>Maple Thrill Park | Packages available<br>from June 30 - September 18, 2022</p></div>
    <div class="promo"><h3>Aurora Coast Family Cruise...<br>The Season's Leading All-<br>Ages Voyage at Sea</h3><p>2022-2024 Sailings | Norway &amp; Iceland<br>Fjords | Offer Expires January 16, 2023</p></div>
    <div class="promo"><h3>Quality Time is the<br>Best Time</h3><p>Northwind Air is celebrating its 35th<br>anniversary!</p></div>
  </div>
</section>

<section class="magazines">
  <h2 class="section-title">Award Winning Magazines</h2>
  <p class="section-sub" style="font-size:14px">Click the magazine cover of your choice to read more.</p>
  <div class="photo-row">
    <div class="photo" role="img" aria-label="Travel magazine cover with sunflowers and red tassels" style="background:linear-gradient(180deg,#3b3a2a 0%,#c9a23a 40%,#b5483a 75%,#6a3a2c 100%)"></div>
    <div class="photo" role="img" aria-label="Luxury travel magazine cover with an infinity pool and palms" style="background:linear-gradient(180deg,#d7b98f 0%,#7fa0a4 40%,#1f6b74 75%,#103f48 100%)"></div>
    <div class="photo" role="img" aria-label="Cruise magazine cover with a couple on a ship deck at sunset" style="background:linear-gradient(180deg,#8fa9c0 0%,#c9b8a2 40%,#6d6f7a 75%,#2e4a6a 100%)"></div>
  </div>
  <span class="btn">VIEW ALL</span>
</section>

<footer class="site-footer">
  <div class="brand"><span class="brand-dot"></span><span>Brisk Harbor Getaways</span></div>
  <nav class="footer-nav"><span>About Us</span><span>Experiences</span><span>Tours</span><span>Offers</span><span>Blogs</span><span>Contest</span><span>Testimonials</span><span>Exclusives</span><span>Contact</span></nav>
  <div class="social"><span>Share</span><span>Follow</span><span>Post</span></div>
  <div class="footer-rule"></div>
  <p class="copyright">©Copyrights 2022 Brisk Harbor Getaways &nbsp;| &nbsp; All Rights Reserved</p>
</footer>
</body>
</html>
```